Harbor Quill Associates Flyer

Create a tri-fold brochure for Harbor Quill Associates. I am getting a new logo - waiting on the final file. I've attached the copy.

Target Market(s)

retail energy companies and retail energy brokers

Industry/Entity Type

energy

Font styles to use
Serif

Colors
0054AA
0677BA
7BADD7
CADEEF
E8F1F8

Requirements
Must have
• I will be uploading a picture of myself and my partner - that should be somewhere in the inside.
Nice to have
• follow the color scheme of the logo
Should not have
• no mine pictures -use energy pictures - power lines etc. office picture and picture of 2 businesspeople shaking hands

```html
<!DOCTYPE html>
<html lang="en">
<head>
<meta charset="utf-8">
<title>Harbor Quill Associates – Tri-fold Brochure</title>
<link rel="stylesheet" href="https://fonts.googleapis.com/css2?family=Arimo:wght@400;700&family=Cinzel:wght@600;700&family=Oswald:wght@400;500&display=swap">
<style>
:root{
  --navy:#0054AA;
  --blue:#0677BA;
  --sky:#7BADD7;
  --mist:#CADEEF;
  --ice:#E8F1F8;
  --ink:#1b1b1b;
  --page:#d3d3d3;
  --white:#ffffff;
}
*{margin:0;padding:0;box-sizing:border-box}
html,body{width:1200px;height:2830px;overflow:hidden;background:var(--page)}
body{position:relative;font-family:"Arimo",Arial,sans-serif;color:var(--ink)}
.spread{position:absolute;left:90px;width:1020px;box-shadow:0 30px 40px -20px rgba(0,0,0,.45);overflow:hidden}
.spread--outside{top:626px;height:726px}
.spread--inside{top:1478px;height:727px}
.panel{position:absolute;overflow:hidden}
.photo{position:absolute}

/* outside spread */
.talent{left:0;top:0;width:343px;height:456px;background:linear-gradient(160deg,#0a66bf 0%,var(--navy) 60%,#0a4a98 100%);color:var(--white);padding:42px 0 0 38px}
.talent__building{position:absolute;right:0;top:100px;width:200px;height:356px;background:linear-gradient(180deg,rgba(123,173,215,.0),rgba(123,173,215,.35));clip-path:polygon(35% 8%,100% 0,100% 100%,0 100%)}
.talent__title{position:relative;font-family:"Cinzel",serif;font-weight:600;color:var(--mist);font-size:21px;line-height:1;letter-spacing:.5px}
.talent__title span{display:block;font-size:31px;color:var(--white);margin-top:2px}
.talent__list{position:relative;list-style:none;margin-top:22px}
.talent__list li{display:flex;align-items:center;gap:14px;font-size:15px;height:33.2px}
.talent__list svg{width:13px;height:13px;flex:none}

.reviews{left:343px;top:0;width:331px;height:456px;background:linear-gradient(180deg,var(--sky) 0%,var(--mist) 100%);padding:36px 32px 0 32px}
.reviews__title{font-family:"Cinzel",serif;font-weight:700;font-size:18.5px;line-height:1.25;color:#10203a;margin-bottom:10px}
.review{font-size:9.6px;line-height:1.32;color:#1d2a3a;padding:10px 0 11px;border-bottom:1px solid #6a8fb3}
.review:first-of-type{padding-top:0}
.review:last-of-type{border-bottom:none}
.review cite{display:block;font-style:normal;font-weight:700;margin-top:3px}

.cover-top{left:674px;top:0;width:346px;height:450px;background:var(--white)}
.brand{display:flex;align-items:center;justify-content:center;gap:8px;font-family:"Cinzel",serif;font-weight:700;color:#111}
.brand__dot{border-radius:50%;background:var(--navy);flex:none}
.cover-top .brand{position:absolute;top:58px;left:0;width:346px;font-size:19px}
.cover-top .brand__dot{width:22px;height:22px}
.cover-top .photo{left:0;top:160px;width:346px;height:290px;background:linear-gradient(180deg,#c9ccd0 0%,#7c8796 55%,#2e3a4f 100%)}

.lineworkers{left:0;top:456px;width:343px;height:270px;background:linear-gradient(160deg,#e9edf2 0%,#b9c4cf 60%,#8b97a4 100%)}
.contact{left:343px;top:456px;width:331px;height:270px;background:var(--ice);text-align:center}
.contact .brand{margin-top:44px;font-size:15px}
.contact .brand__dot{width:16px;height:16px}
.contact__phone{font-family:"Cinzel",serif;font-weight:700;font-size:27px;margin-top:52px;letter-spacing:.5px}
.contact__line{font-size:15px;margin-top:12px}
.contact__line + .contact__line{margin-top:10px}

.cover-title{left:674px;top:450px;width:346px;height:276px;background:linear-gradient(160deg,#0a6bc4 0%,var(--navy) 100%);color:var(--white);text-align:center;padding-top:48px}
.cover-title__main{font-family:"Oswald",sans-serif;font-weight:400;font-size:42px;line-height:1.05;letter-spacing:.3px}
.cover-title__tag{display:inline-block;margin-top:8px;background:var(--sky);color:#0b1d3a;font-family:"Cinzel",serif;font-weight:700;font-size:23px;padding:3px 14px;width:272px}
.cover-title__web{font-size:15px;margin-top:22px}

/* inside spread */
.founders{left:0;top:0;width:343px;height:406px;background:linear-gradient(180deg,#bfd3e8 0%,#8e9ba9 55%,#5b6470 100%)}
.about{left:0;top:406px;width:343px;height:321px;background:var(--white);padding:0 34px}
.about .brand{margin-top:38px;justify-content:flex-start;font-size:15px}
.about .brand__dot{width:16px;height:16px}
.about__title{font-family:"Cinzel",serif;font-weight:700;color:var(--navy);font-size:32px;line-height:1.05;margin-top:36px}
.about__text{font-size:12.2px;line-height:1.45;margin-top:16px}

.gallery{left:343px;top:0;width:331px;height:406px;background:linear-gradient(160deg,#0a6bc4 0%,var(--navy) 100%)}
.gallery .photo{left:32px;width:272px;border:3px solid var(--white);border-radius:16px}
.gallery__handshake{top:40px;height:130px;background:linear-gradient(135deg,#8fa0b3 0%,#d9dde3 55%,#a6b1bd 100%)}
.gallery__grid{top:212px;height:130px;background:linear-gradient(180deg,#c8dbef 0%,#8fb3d8 55%,#3d5f85 100%)}

.mission{left:674px;top:0;width:346px;height:406px;background:linear-gradient(160deg,#0a6bc4 0%,var(--navy) 100%);color:var(--white);padding:56px 40px 0 32px;font-size:12.6px;line-height:1.42}

.consulting{left:343px;top:406px;width:677px;height:321px;background:var(--white)}
.consulting .photo{left:180px;top:0;width:497px;height:321px;background:linear-gradient(90deg,rgba(255,255,255,1) 0%,rgba(255,255,255,0) 28%),linear-gradient(160deg,#dfe6ee 0%,#6f83a0 50%,#2d3b55 100%)}
.consulting__text{position:absolute;left:32px;top:42px;width:275px;font-size:12.4px;line-height:1.42}
</style>
</head>
<body>

<section class="spread spread--outside" aria-label="Brochure outside">
  <div class="panel talent">
    <div class="talent__building" role="img" aria-label="Faint photo of a glass office tower"></div>
    <h2 class="talent__title">Great Talent<span>Available For</span></h2>
    <ul class="talent__list">
      <li><svg viewBox="0 0 14 14"><circle cx="7" cy="7" r="7" fill="#CADEEF"/><path d="M3.8 7.2l2.1 2.1 4.3-4.4" stroke="#0054AA" stroke-width="1.8" fill="none"/></svg>Accounting/Finance</li>
      <li><svg viewBox="0 0 14 14"><circle cx="7" cy="7" r="7" fill="#CADEEF"/><path d="M3.8 7.2l2.1 2.1 4.3-4.4" stroke="#0054AA" stroke-width="1.8" fill="none"/></svg>Channel Management</li>
      <li><svg viewBox="0 0 14 14"><circle cx="7" cy="7" r="7" fill="#CADEEF"/><path d="M3.8 7.2l2.1 2.1 4.3-4.4" stroke="#0054AA" stroke-width="1.8" fill="none"/></svg>Customer Service</li>
      <li><svg viewBox="0 0 14 14"><circle cx="7" cy="7" r="7" fill="#CADEEF"/><path d="M3.8 7.2l2.1 2.1 4.3-4.4" stroke="#0054AA" stroke-width="1.8" fill="none"/></svg>Operations</li>
      <li><svg viewBox="0 0 14 14"><circle cx="7" cy="7" r="7" fill="#CADEEF"/><path d="M3.8 7.2l2.1 2.1 4.3-4.4" stroke="#0054AA" stroke-width="1.8" fill="none"/></svg>Pricing Analysts</li>
      <li><svg viewBox="0 0 14 14"><circle cx="7" cy="7" r="7" fill="#CADEEF"/><path d="M3.8 7.2l2.1 2.1 4.3-4.4" stroke="#0054AA" stroke-width="1.8" fill="none"/></svg>Regulatory/Compliance</li>
      <li><svg viewBox="0 0 14 14"><circle cx="7" cy="7" r="7" fill="#CADEEF"/><path d="M3.8 7.2l2.1 2.1 4.3-4.4" stroke="#0054AA" stroke-width="1.8" fill="none"/></svg>Sales/Marketing</li>
      <li><svg viewBox="0 0 14 14"><circle cx="7" cy="7" r="7" fill="#CADEEF"/><path d="M3.8 7.2l2.1 2.1 4.3-4.4" stroke="#0054AA" stroke-width="1.8" fill="none"/></svg>Scheduling</li>
      <li><svg viewBox="0 0 14 14"><circle cx="7" cy="7" r="7" fill="#CADEEF"/><path d="M3.8 7.2l2.1 2.1 4.3-4.4" stroke="#0054AA" stroke-width="1.8" fill="none"/></svg>Supply Experts</li>
    </ul>
  </div>

  <div class="panel reviews">
    <h2 class="reviews__title">Here’s what some of<br>our clients are saying:</h2>
    <blockquote class="review">“Dorian Vale &amp; Harbor Quill Associates found us the perfect candidate and they did it quickly. If you’re an REP looking for great talent, you should use HQA”<cite>- Tom Brandell, BrightField Energy</cite></blockquote>
    <blockquote class="review">“Harbor Quill Associates helped TPS quickly find a great candidate for an essential position that we need to fill right away”.<cite>- Nadia Corwin, Tailored Power Services</cite></blockquote>
    <blockquote class="review">“Harbor Quill Associates helped Halvern quickly find a great person for our team. Dorian Vale has more connections than just about anyone else in the industry”.<cite>- Glen Ashford, Halvern Energy</cite></blockquote>
    <blockquote class="review">“Meterwise brought on Dorian Vale and Harbor Quill Associates to help us find an amazing VP of Sales. Because of Dorian’s extensive contacts in the retail energy industry, he was able to find the right person for this important role - and he did it quickly”.<cite>- Paul Denning, Meterwise</cite></blockquote>
  </div>

  <div class="panel cover-top">
    <div class="brand"><span class="brand__dot"></span>Harbor Quill Associates</div>
    <div class="photo" role="img" aria-label="Photo of two businessmen shaking hands outside an office building"></div>
  </div>

  <div class="panel lineworkers" role="img" aria-label="Photo of two line workers in hard hats on a utility pole among power lines"></div>

  <div class="panel contact">
    <div class="brand"><span class="brand__dot"></span>Harbor Quill Associates</div>
    <p class="contact__phone">555.014.2270</p>
    <p class="contact__line">dorian@harborquillassoc.com</p>
    <p class="contact__line">harborquillassoc.com</p>
  </div>

  <div class="panel cover-title">
    <h1 class="cover-title__main">RETAIL ENERGY<br>RECRUITING AND</h1>
    <p class="cover-title__tag">M&amp;A CONSULTING</p>
    <p class="cover-title__web">harborquillassoc.com</p>
  </div>
</section>

<section class="spread spread--inside" aria-label="Brochure inside">
  <div class="panel founders" role="img" aria-label="Portrait photo of the two founding partners, a woman and a man"></div>

  <div class="panel about">
    <div class="brand"><span class="brand__dot"></span>Harbor Quill Associates</div>
    <h2 class="about__title">Harbor Quill<br>Associates</h2>
    <p class="about__text">is the 4th company in the retail energy space started by Dorian &amp; Maren Vale. Dorian &amp; Maren have been in the retail energy space for more than <strong>25 years and are two of the most connected people in the industry.</strong></p>
  </div>

  <div class="panel gallery">
    <div class="photo gallery__handshake" role="img" aria-label="Close-up photo of a business handshake"></div>
    <div class="photo gallery__grid" role="img" aria-label="Photo of solar panels, a transmission tower and wind turbines"></div>
  </div>

  <div class="panel mission">
    <p>Harbor Quill Associates is also retail energy’s most used recruiter. HQA is the only recruiting company focused exclusively on the retail energy industry. Since our inception in 2022, HQA has filled over 35 roles - including sales, channel management, pricing, billing, supply, regulatory etc. Harbor Quill Associates works quickly and we can find great talent from analyst level positions right up to the most critical C-level jobs. We help REPs, brokers and retail energy industry vendors find the great people they need to keep growing. Harbor Quill Associates only works with experienced retail energy professionals.</p>
  </div>

  <div class="panel consulting">
    <div class="photo" role="img" aria-label="Photo of two colleagues reviewing work on a laptop in an office"></div>
    <p class="consulting__text">Harbor Quill Associates helps companies in two ways. First, HQA is an experienced M&amp;A consulting firm. Whether you’re looking to buy or sell, we can connect you with buyers and sellers that match your target profile. We work with REPs, brokers and retail energy vendors of all types. We’re not investment bankers, but we’re better connected and charge much less. In the last 12 months, HQA has made the introductions for 3 significant transactions. If now is the right time for a strategic move, we can help.</p>
  </div>
</section>

</body>
</html>
```